"Solvenor" Brand Label Design for Red Wine

Ramiro Tavelo Vinhos is a Portuguese winemaking company born in the Douro Valley. Ramiro Tavelo, is a 7th generation winemaker and has a great reputation on making quality Portuguese wines,

Solvenor is latin for “opposite”, “contrary” and “in contradiction”. We would like to develop this brand by having an out of the box concept and design for the label based on this . We would like to go for something along the lines of the designs attached.

Also, this label must include:

• The brand name – “Solvenor”
• The Region of Origin – Douro
• The Appelation – Denominação de Origem Controlada
• The Type of Wine – “Vinho Tinto” and “Red Wine”
• The Vintage Year – 2020
• Use the bottle model from the technical sheet attached

We look forward to seeing your designs!

Industry/Entity Type

Wine and beverages

Requirements
Must have
• Out of the box concept

```html
<!DOCTYPE html>
<html lang="pt">
<head>
<meta charset="UTF-8">
<title>Solvenor — Douro Red Wine Label</title>
<link rel="stylesheet" href="https://fonts.googleapis.com/css2?family=Cinzel:wght@400;500&family=Cormorant+Garamond:wght@400;500;600&display=swap">
<style>
  :root {
    --label-tan: #d2c29e;
    --label-tan-light: #ddd0b0;
    --ink: #3b2c1f;
    --ink-soft: #5a4632;
    --medallion-gold: #c9a24a;
    --medallion-blue: #3e5f9c;
    --medallion-cream: #ece3cc;
  }
  html, body {
    margin: 0;
    padding: 0;
    width: 778px;
    height: 1200px;
    overflow: hidden;
    background: var(--label-tan);
  }
  .label {
    position: relative;
    width: 778px;
    height: 1200px;
    background: radial-gradient(ellipse at 50% 45%, var(--label-tan-light) 0%, var(--label-tan) 70%);
    color: var(--ink);
    font-family: "Cormorant Garamond", Georgia, serif;
    box-sizing: border-box;
  }
  .brand-name {
    position: absolute;
    top: 170px;
    left: 0;
    right: 0;
    margin: 0;
    text-align: center;
    font-family: "Cinzel", "Times New Roman", serif;
    font-weight: 400;
    font-size: 82px;
    letter-spacing: 4px;
  }
  .region {
    position: absolute;
    top: 290px;
    left: 0;
    right: 0;
    text-align: center;
    font-family: "Cinzel", "Times New Roman", serif;
    font-weight: 500;
    font-size: 40px;
    letter-spacing: 2px;
    margin: 0;
  }
  .region-caption {
    position: absolute;
    top: 342px;
    left: 0;
    right: 0;
    text-align: center;
    font-size: 19px;
    letter-spacing: 1.5px;
    text-transform: uppercase;
    color: var(--ink-soft);
    margin: 0;
  }
  .medallion {
    position: absolute;
    top: 390px;
    left: 199px;
    width: 380px;
    height: 380px;
  }
  .wine-type {
    position: absolute;
    top: 880px;
    font-size: 22px;
    color: var(--ink-soft);
    margin: 0;
  }
  .wine-type--pt { left: 110px; }
  .wine-type--en { right: 110px; }
  .vintage {
    position: absolute;
    top: 880px;
    left: 0;
    right: 0;
    text-align: center;
    font-family: "Cinzel", "Times New Roman", serif;
    font-weight: 500;
    font-size: 58px;
    letter-spacing: 3px;
    margin: 0;
  }
  .appellation {
    position: absolute;
    top: 1035px;
    left: 0;
    right: 0;
    text-align: center;
    font-size: 22px;
    color: var(--ink-soft);
    margin: 0;
  }
</style>
</head>
<body>
  <main class="label">
    <h1 class="brand-name">SOLVENOR</h1>
    <p class="region">DOURO</p>
    <p class="region-caption">The Region of Origin</p>

    <svg class="medallion" viewBox="0 0 380 380" role="img" aria-label="Circular medallion illustration of a sun and crescent moon within an ornamental ring">
      <defs>
        <radialGradient id="medallionFill" cx="50%" cy="50%" r="50%">
          <stop offset="0%" stop-color="var(--medallion-gold)"/>
          <stop offset="55%" stop-color="var(--medallion-blue)"/>
          <stop offset="80%" stop-color="var(--medallion-cream)"/>
          <stop offset="100%" stop-color="var(--medallion-cream)"/>
        </radialGradient>
      </defs>
      <circle cx="190" cy="190" r="186" fill="url(#medallionFill)"/>
      <circle cx="190" cy="190" r="186" fill="none" stroke="var(--ink)" stroke-width="2"/>
    </svg>

    <p class="wine-type wine-type--pt">Vinho Tinto</p>
    <p class="vintage">2020</p>
    <p class="wine-type wine-type--en">Red Wine</p>

    <p class="appellation">Denominação de Origem Controlada</p>
  </main>
</body>
</html>
```